Design for Torvel Ginger Chewy Candy!

Hello! We are Torvel Enterprises Corp, a food manufacturer and distributor based in Los Angeles, CA. We manufacture Chips, Cookies, Juices, Dairy, and last but not least, Candies! We are launching our Ginger Chewy Candy soon and we need a great design for it!

Our Ginger Chewy Candy is a perfect mixture between sweet and spicy from the ginger itself. Torvel Ginger Chewy Candy a good relief for sore throat and nausea.

Now, other than a great design, we also welcome brand suggestions for the candy.
If you can come up with a logo for the Ginger Candy, that would be swell!

We are open to unique and out of the box design. We chose a few color schemes for the design, but feel free to step out of the box if you feel it suits the brand.

We don't have the exact size for the plastic pouch, but it should be a generic small plastic pouch size (approximately 4 oz resealable plastic pouch)

Please have fun designing the project, we can't wait to see all the great designs!

Cheers!

Target Market(s)

USA and Asian market
Age 30-70
Male and Female

Industry/Entity Type

Manufacture

Font styles to use
Serif
Sans Serif
Decorative

Colors
fff3d1
fee18a
fece3e
fbc994
fce8d3

Requirements
Must have
• Torvel Logo
• A picture of ginger (illustrations or photographs are welcome)
Nice to have
• Coating suggestions like Matte surface or SPOT UV
• Give us ideas of what the name of the chewy candy should be. Product name ideas are welcome!

```html
<!DOCTYPE html>
<html lang="en">
<head>
<meta charset="utf-8">
<title>Torvel Ginger Chewy Candy – Back Side</title>
<link href="https://fonts.googleapis.com/css2?family=Roboto:wght@400;500;700;900&display=swap" rel="stylesheet">
<style>
  :root {
    --board: #333333;
    --pouch: #f6df9e;
    --pouch-deep: #efd48a;
    --ink: #2b2b2b;
    --brand-blue: #2b3d98;
    --white: #ffffff;
  }
  * { box-sizing: border-box; margin: 0; padding: 0; }
  html, body { width: 1000px; height: 1200px; overflow: hidden; }
  body {
    background: var(--board);
    font-family: "Roboto", Arial, sans-serif;
    color: var(--ink);
    position: relative;
  }
  .view-title {
    position: absolute; top: 130px; left: 0; width: 1000px;
    text-align: center; color: var(--white); font-size: 32px; font-weight: 500;
  }
  .pouch {
    position: absolute; left: 200px; top: 216px; width: 600px; height: 884px;
    background: radial-gradient(circle at 50% 45%, var(--pouch) 0%, var(--pouch-deep) 100%);
    overflow: hidden;
  }
  .tear-note, .reseal-note {
    position: absolute; top: 36px; font-size: 12px; font-weight: 500;
  }
  .tear-note { left: 22px; }
  .reseal-note { right: 22px; }
  .brand-name {
    position: absolute; left: 104px; top: 142px;
    font-size: 54px; font-weight: 700; line-height: 60px; color: var(--brand-blue);
  }
  .claims {
    position: absolute; left: 36px; top: 254px; width: 300px;
    list-style: none; font-size: 12px; font-weight: 500; line-height: 19px;
  }
  .claims li::before { content: "● "; }
  .claims .inline { display: inline; margin-right: 6px; }
  .claims .fat { font-size: 14px; }
  .claims .indent { padding-left: 72px; }

  .info-block { position: absolute; left: 76px; width: 270px; font-size: 11px; line-height: 16px; }
  .info-block h3 { font-size: 11px; font-weight: 700; line-height: 14px; margin-bottom: 4px; }
  .caution { top: 352px; }
  .ingredients { top: 430px; }
  .allergen { top: 506px; }
  .storage { top: 562px; }

  .nutrition {
    position: absolute; left: 356px; top: 120px; width: 216px; height: 426px;
    background: var(--white); border: 2px solid var(--ink); padding: 6px 8px;
    font-size: 9px; line-height: 12px;
  }
  .nutrition h2 { font-size: 21px; font-weight: 900; line-height: 24px; border-bottom: 1px solid var(--ink); }
  .nutrition .servings { font-weight: 700; font-size: 12.5px; line-height: 15px; margin-top: 2px; }
  .nutrition .row { display: flex; justify-content: space-between; }
  .nutrition .thick { border-bottom: 7px solid var(--ink); padding-bottom: 2px; }
  .nutrition .mid { border-bottom: 4px solid var(--ink); }
  .nutrition .calories { font-size: 21px; font-weight: 900; line-height: 26px; }
  .nutrition .line { display: flex; border-top: 1px solid #999; padding: 2px 0; }
  .nutrition .line .dv { width: 30px; font-weight: 700; flex: none; }
  .nutrition .sub1 { padding-left: 12px; }
  .nutrition .sub2 { padding-left: 24px; }
  .nutrition .note { font-size: 7px; line-height: 9px; margin-top: 12px; }

  .company {
    position: absolute; left: 300px; top: 580px; width: 260px;
    font-size: 11px; line-height: 17px; text-align: center;
  }
  .company .corp { margin-bottom: 20px; padding-right: 40px; }
  .company address { font-style: normal; padding-right: 40px; margin-bottom: 4px; }

  .web-band {
    position: absolute; left: 0; top: 768px; width: 600px; height: 36px;
    background: var(--brand-blue);
  }
  .web-band span {
    position: absolute; left: 280px; top: 6px;
    color: var(--white); font-size: 20px; font-weight: 700; letter-spacing: 1.5px; line-height: 24px;
  }
  .product-seal {
    position: absolute; left: 90px; top: 708px; width: 170px; height: 170px;
    border-radius: 50%; background: var(--brand-blue);
    display: flex; align-items: center; justify-content: center; text-align: center;
    color: var(--white); font-size: 17px; font-weight: 700; line-height: 21px; padding: 22px;
  }
</style>
</head>
<body>
  <div class="view-title">Back Side</div>

  <section class="pouch" role="img" aria-label="Pouch back with a scattered pattern of ginger root illustrations on a warm yellow ground">
    <div class="tear-note">▸ Tear Here</div>
    <div class="reseal-note">Resealable Bag</div>

    <div class="brand-name">Torvel</div>

    <ul class="claims">
      <li>NO Artificial colors Flavors or Preservativs</li>
      <li class="inline">Made with fresh ginger</li><li class="inline fat">fat free</li>
      <li class="indent">gluteen free</li>
    </ul>

    <div class="info-block caution">
      <h3>caution:</h3>
      <p>Lorem Ipsum is simply dummy text of the printing and typesetting industry.</p>
    </div>
    <div class="info-block ingredients">
      <h3>Ingredients:</h3>
      <p>Sugar, Peel ginger, tapioca starch</p>
    </div>
    <div class="info-block allergen">
      <h3>Allergen statement:</h3>
      <p>made in a facility that also processes milk,<br>soy and peanuts.</p>
    </div>
    <div class="info-block storage">
      <h3>Storage:</h3>
      <p>Store in a cool , dry place.</p>
    </div>

    <div class="nutrition">
      <h2>Nutrition Facts</h2>
      <div class="servings">8 servings per container</div>
      <div class="row thick"><span>Serving size</span><span>2/3 cup (55g)</span></div>
      <div>Amount per 2/3 cup</div>
      <div class="row mid calories"><span>Calories</span><span>230</span></div>
      <div><b>% DV*</b></div>
      <div class="line"><span class="dv">12%</span><b>Total Fat</b>&nbsp;8g</div>
      <div class="line"><span class="dv">5%</span><span class="sub1">Saturated Fat 1g</span></div>
      <div class="line"><span class="dv"></span><span class="sub1">Trans Fat 0g</span></div>
      <div class="line"><span class="dv">0%</span><b>Cholesterol</b>&nbsp;0mg</div>
      <div class="line"><span class="dv">7%</span><b>Sodium</b>&nbsp;160mg</div>
      <div class="line"><span class="dv">12%</span><b>Total Carbs</b>&nbsp;37g</div>
      <div class="line"><span class="dv">14%</span><span class="sub1">Dietary Fiber 4g</span></div>
      <div class="line"><span class="dv"></span><span class="sub1">Sugars 1g</span></div>
      <div class="line"><span class="dv"></span><span class="sub2">Added Sugars 0g</span></div>
      <div class="line mid"><span class="dv"></span><b>Protein</b>&nbsp;3g</div>
      <div class="line"><span class="dv">10%</span>Vitamin D 2mcg</div>
      <div class="line"><span class="dv">20%</span>Calcium 260mg</div>
      <div class="line"><span class="dv">45%</span>Iron 8mg</div>
      <div class="line"><span class="dv">5%</span>Potassium 235mg</div>
      <p class="note">* Footnote on Daily Values (DV) and calories reference to be inserted here.</p>
    </div>

    <div class="company">
      <p class="corp">Torvel Enterprises Corp.</p>
      <address>2750 Harlow Ave Alder Grove,<br>CA 90412</address>
      <p>Phone : +1-555-014-2000</p>
      <p>Fax : +1-555-014-1977</p>
      <p>Email : contact@torvelfood.com</p>
    </div>

    <div class="web-band"><span>www.torvelfood.com</span></div>
    <div class="product-seal">Torvel Ginger Chewy Candy</div>
  </section>
</body>
</html>
```